Kem7Dex Letterhead

Need a new letterhead for my law firm.
IDENTIFYING INFORMATION BELOW:
Ansel T Brightwater III
Attorney at Law
Address: 4832 Tillbury Rd, Ste 250, Dallas, TX 75204
Phone: 866-402-7183
Fax: 469-583-0271
Email: kem@kem7dex.example
Website: www.kem7dex.example

Colors
0054AA
0677BA
7BADD7
CADEEF
E8F1F8

Requirements
Must have
• Logo needs to be on the letterhead, along with identifying information which is included in the project description.

```html
<!DOCTYPE html>
<html lang="en">
<head>
<meta charset="utf-8">
<title>Kem7Dex Letterhead</title>
<link rel="stylesheet" href="https://fonts.googleapis.com/css2?family=Lato:wght@400;700&family=Open+Sans:wght@400&display=swap">
<style>
  :root {
    --ink: #1b1b1b;
    --body: #4a4a4a;
    --brand-blue: #0054AA;
    --brand-mid: #0677BA;
    --brand-light: #7BADD7;
    --rule: #cfcfcf;
    --backdrop: #e6e7e9;
    --paper: #ffffff;
  }
  * { margin: 0; padding: 0; box-sizing: border-box; }
  html, body { width: 1040px; height: 1200px; overflow: hidden; background: var(--backdrop); }
  .letterhead {
    position: absolute; left: 80px; top: 33px; width: 881px; height: 1133px;
    background: var(--paper); box-shadow: 0 2px 10px rgba(0,0,0,.12);
    font-family: "Open Sans", sans-serif; color: var(--body);
  }
  .band { position: absolute; left: 0; width: 881px; height: 20px; display: block; }
  .band-top { top: 0; }
  .band-bottom { bottom: 0; }
  .brand-name {
    position: absolute; left: 69px; top: 42px;
    font-family: "Lato", sans-serif; font-weight: 700; font-size: 34px; letter-spacing: 1px;
    color: var(--ink); line-height: 40px;
  }
  .attorney { position: absolute; right: 91px; top: 42px; text-align: right; font-family: "Lato", sans-serif; }
  .attorney-name { font-size: 19px; font-weight: 700; color: var(--brand-blue); line-height: 22px; }
  .attorney-title { font-size: 16px; color: var(--ink); line-height: 20px; }
  .block { position: absolute; left: 83px; width: 712px; font-size: 14px; }
  .issue-date { top: 210px; line-height: 20px; }
  .recipient { top: 245px; line-height: 17px; }
  .salutation { top: 342px; line-height: 20px; }
  .para { line-height: 25.3px; text-align: justify; font-size: 13.7px; }
  .para-1 { top: 390px; }
  .para-2 { top: 542px; }
  .para-3 { top: 644px; }
  .closing { top: 774px; line-height: 20px; }
  .signature-mark {
    position: absolute; left: 83px; top: 812px; width: 202px; height: 22px;
    background: linear-gradient(90deg, #e4e4e4, #f2f2f2); border-radius: 3px;
  }
  .signer-name { top: 849px; font-size: 17.5px; color: #333; line-height: 22px; }
  .signer-role { top: 878px; line-height: 20px; }
  .footer { position: absolute; left: 0; width: 881px; text-align: center; font-family: "Lato", sans-serif; color: var(--ink); }
  .footer-address { top: 1054px; font-size: 16.5px; line-height: 20px; }
  .footer-rule { position: absolute; left: 140px; top: 1076px; width: 600px; height: 1px; background: var(--rule); }
  .footer-contact { top: 1081px; font-size: 16.5px; line-height: 20px; }
  .footer-contact .label { color: var(--brand-blue); font-weight: 700; }
</style>
</head>
<body>
<div class="letterhead">
  <svg class="band band-top" viewBox="0 0 881 20" aria-hidden="true">
    <defs>
      <linearGradient id="topBlue" x1="0" x2="1" y1="0" y2="0">
        <stop offset="0" stop-color="#0677BA"/><stop offset="1" stop-color="#0054AA"/>
      </linearGradient>
    </defs>
    <polygon points="0,0 429,0 410,20 0,20" fill="#1b1b1b"/>
    <polygon points="438,0 881,0 881,20 419,20" fill="url(#topBlue)"/>
  </svg>

  <div class="brand-name">KEM7DEX</div>
  <div class="attorney">
    <div class="attorney-name">Ansel T Brightwater III</div>
    <div class="attorney-title">Attorney at Law</div>
  </div>

  <p class="block issue-date">Issuing Date: May 5, 2018</p>
  <p class="block recipient">Name Of Employee Mr. XYZABC<br>Address of Employee<br>Address Line 2 etc..</p>
  <p class="block salutation">Dear Mr.XYZABC</p>

  <p class="block para para-1">Lorem Ipsum has been the industry's standard dummy text ever since the 1500s, when an unknown printer took a galley of type and scrambled it to make a type specimen book. It has survived not only five centuries, but also the leap into electronic typesetting, remaining essentially unchanged. It was popularised in the 1960s with the release of Tessaline sheets containing Lorem Ipsum passages, and more recently with desktop publishing software like Orvane PageSetter including versions of Lorem Ipsum.</p>
  <p class="block para para-2">Lorem Ipsum is simply dummy text of the printing and typesetting industry. Lorem Ipsum has been the industry's standard dummy text ever since the 1500s, when an unknown printer took a galley of type and scrambled it to make a type specimen book.</p>
  <p class="block para para-3">It has survived not only five centuries, but also the leap into electronic typesetting, remaining essentially unchanged. It was popularised in the 1960s with the release of Tessaline sheets containing Lorem IpsumIpsum passages.</p>

  <p class="block closing">Yours Sincerely</p>
  <div class="signature-mark" role="img" aria-label="Handwritten signature of the sender"></div>
  <p class="block signer-name">Marcus Ellery</p>
  <p class="block signer-role">Managing Director</p>

  <p class="footer footer-address">4832 Tillbury Rd, Ste 250, Dallas, TX 75204</p>
  <div class="footer-rule"></div>
  <p class="footer footer-contact"><span class="label">P:</span> 866-402-7183 &nbsp;|&nbsp; <span class="label">F:</span> 469-583-0271 | <span class="label">E:</span> kem@kem7dex.example &nbsp;|&nbsp; <span class="label">W:</span> www.kem7dex.example</p>

  <svg class="band band-bottom" viewBox="0 0 881 20" aria-hidden="true">
    <defs>
      <linearGradient id="bottomBlue" x1="0" x2="1" y1="0" y2="0">
        <stop offset="0" stop-color="#0677BA"/><stop offset="1" stop-color="#1a93d2"/>
      </linearGradient>
    </defs>
    <polygon points="0,0 454,0 436,20 0,20" fill="#1b1b1b"/>
    <polygon points="463,0 881,0 881,20 445,20" fill="url(#bottomBlue)"/>
  </svg>
</div>
</body>
</html>
```